Business Card Design Project

We are an agricultural business based in Brisbane.
We design, manage and operate regional saleyards. Our logo is green/silver in colour and details of our business can be found on our website www.vodemarketyards.com.au

Just wanting a corporate design for some business cards and include name, position, contact details.

Thanks

Industry/Entity Type

Business

```html
<!DOCTYPE html>
<html lang="en">
<head>
<meta charset="utf-8">
<title>Vode Market Yards – Business Card</title>
<link rel="stylesheet" href="https://fonts.googleapis.com/css2?family=PT+Sans+Narrow:wght@700&family=Arimo:wght@400&display=swap">
<style>
  :root {
    --backdrop: #2b2b2b;
    --card-white: #ffffff;
    --brand-green: #00873c;
    --brand-silver: #9a9a9a;
    --ink: #231f20;
    --on-green: #ffffff;
  }
  html, body {
    margin: 0;
    width: 1200px;
    height: 797px;
    overflow: hidden;
    background: var(--backdrop);
  }
  .canvas {
    position: relative;
    width: 1200px;
    height: 797px;
  }
  .business-card {
    position: absolute;
    left: 170px;
    top: 153px;
    width: 860px;
    height: 490px;
    background: var(--card-white);
    overflow: hidden;
    box-shadow: 0 6px 18px rgba(0,0,0,0.45);
  }
  .card-panel {
    position: absolute;
    inset: 0;
  }
  .brand-name {
    position: absolute;
    left: 40px;
    top: 178px;
    width: 380px;
    margin: 0;
    text-align: center;
    font-family: "PT Sans Narrow", "Arial Narrow", sans-serif;
    font-weight: 700;
    font-size: 54px;
    line-height: 56px;
    letter-spacing: 1px;
    color: var(--ink);
    text-transform: uppercase;
  }
  .holder-name {
    position: absolute;
    left: 512px;
    top: 20px;
    margin: 0;
    font-family: "PT Sans Narrow", "Arial Narrow", sans-serif;
    font-weight: 700;
    font-size: 46px;
    color: var(--on-green);
    white-space: nowrap;
  }
  .holder-role {
    position: absolute;
    left: 514px;
    top: 78px;
    margin: 0;
    font-family: "Arimo", Arial, sans-serif;
    font-size: 23px;
    color: var(--on-green);
    white-space: nowrap;
  }
  .contact-list {
    position: absolute;
    left: 512px;
    top: 372px;
    margin: 0;
    padding: 0;
    list-style: none;
    font-family: "Arimo", Arial, sans-serif;
    font-size: 18px;
    color: var(--on-green);
  }
  .contact-item {
    display: flex;
    align-items: center;
    height: 36px;
    white-space: nowrap;
  }
  .contact-icon {
    flex: none;
    width: 26px;
    height: 22px;
    margin-right: 12px;
    fill: none;
    stroke: var(--on-green);
    stroke-width: 1.8;
  }
</style>
</head>
<body>
<main class="canvas">
  <article class="business-card">
    <svg class="card-panel" viewBox="0 0 860 490" width="860" height="490" aria-hidden="true">
      <path d="M445 0 Q475 245 448 490 L465 490 Q492 245 462 0 Z" fill="var(--brand-silver)"/>
      <path d="M462 0 Q492 245 465 490 L860 490 L860 0 Z" fill="var(--brand-green)"/>
    </svg>

    <h1 class="brand-name">Vode Market<br>Yards</h1>

    <h2 class="holder-name">Daniel Harper</h2>
    <p class="holder-role">Managing Director</p>

    <ul class="contact-list">
      <li class="contact-item">
        <svg class="contact-icon" viewBox="0 0 28 24"><rect x="2" y="4" width="24" height="16"/><path d="M2 4 L14 14 L26 4"/></svg>
        daniel@vodemarketyards.com.au
      </li>
      <li class="contact-item">
        <svg class="contact-icon" viewBox="0 0 28 24"><circle cx="14" cy="12" r="10"/><path d="M10 8 q-1 5 4 9 l2-2 -2-2 -2 1 q-2-2-1-4 l2-1 -1-2 z"/></svg>
        0400 318 927
      </li>
      <li class="contact-item">
        <svg class="contact-icon" viewBox="0 0 28 24"><circle cx="14" cy="12" r="10"/><path d="M4 12 H24 M14 2 Q8 12 14 22 Q20 12 14 2"/></svg>
        www.vodemarketyards.com.au
      </li>
    </ul>
  </article>
</main>
</body>
</html>
```